Sales Brochure- Generic Line Card 215mm x 140mm

Design a double-sided brochure similar to the attached sample. Cover Page contains a logo and theme that never changes. However, the background picture and the description text on the lower corner will be changed to advertise multiple services. Reverse-side contains Detailed Descriptive text related to the picture on Cover Page as well as Logo and Contact information for the business. Use the Ridgeline Controls website www.ridgelinecontrols.ca for theme, color and contact information. Also, use attached business card design for theme to match. Use the supplied logo. SIZE 215mm x 140mm

Font styles to use
Sans Serif

Colors

Designer to choose colors to be used in the design.

Requirements
Must have
• Look Similar to Sample Brochure but include Ridgeline Controls theme and colors

```html
<!DOCTYPE html>
<html lang="en">
<head>
<meta charset="utf-8">
<title>Ridgeline Controls – CNC Machining Line Card</title>
<link rel="stylesheet" href="https://fonts.googleapis.com/css2?family=Montserrat:wght@300;600;800;900&display=swap">
<style>
  :root {
    --backdrop: #cf6d08;
    --paper: #f6f5f2;
    --teal: #13918c;
    --teal-dark: #0d6f6c;
    --orange: #e4532a;
    --label: #b5502c;
    --ink-dark: #0f1d21;
    --white: #ffffff;
  }
  html, body {
    margin: 0;
    width: 1200px;
    height: 700px;
    overflow: hidden;
    background: var(--backdrop);
  }
  .stage {
    width: 1200px;
    height: 700px;
    display: flex;
    align-items: center;
    justify-content: center;
  }
  .cover {
    width: 960px;
    height: 625px;
    display: block;
    box-shadow: 0 14px 30px rgba(0,0,0,0.28);
  }
  .brand-name { font: 900 50px "Montserrat", sans-serif; fill: var(--white); letter-spacing: 1px; }
  .brand-sub  { font: 600 15px "Montserrat", sans-serif; fill: var(--white); letter-spacing: 14px; }
  .service-label { font: 800 20px "Montserrat", sans-serif; fill: var(--white); letter-spacing: 0.5px; }
  .headline-kicker { font: 300 24px "Montserrat", sans-serif; fill: var(--white); letter-spacing: 1px; }
  .headline-main { font: 900 28px "Montserrat", sans-serif; fill: var(--orange); }
  .web-address { font: 600 17px "Montserrat", sans-serif; fill: var(--white); letter-spacing: 0.5px; }
</style>
</head>
<body>
<main class="stage">
  <svg class="cover" viewBox="0 0 960 625" xmlns="http://www.w3.org/2000/svg" role="group" aria-label="Ridgeline Controls CNC machining brochure cover">
    <defs>
      <linearGradient id="steel" x1="0" y1="0" x2="1" y2="1">
        <stop offset="0" stop-color="#2b3033"/>
        <stop offset="0.5" stop-color="#8a9094"/>
        <stop offset="1" stop-color="#1c2022"/>
      </linearGradient>
      <linearGradient id="dark-panel" x1="0" y1="0" x2="1" y2="1">
        <stop offset="0" stop-color="#16383c"/>
        <stop offset="1" stop-color="#0b1316"/>
      </linearGradient>
    </defs>

    <rect class="paper" width="960" height="625" fill="var(--paper)"/>

    <!-- accent stripe -->
    <polygon class="accent-stripe" points="0,70 540,48 560,82 0,106" fill="var(--orange)"/>

    <!-- brand band -->
    <polygon class="brand-band" points="520,0 960,0 960,100 575,130" fill="var(--teal)"/>
    <rect class="brand-mark" x="585" y="22" width="30" height="30" fill="var(--white)"/>
    <text class="brand-name" x="628" y="56">RIDGELINE</text>
    <text class="brand-sub" x="632" y="84">CONTROLS</text>

    <!-- service photos -->
    <polygon class="photo-lathe" role="img" aria-label="Photo of a lathe turning a polished steel part"
      points="0,195 70,185 330,470 0,520" fill="url(#steel)"/>
    <polygon class="photo-milling" role="img" aria-label="Photo of an end mill cutting metal with flying chips"
      points="105,175 330,148 540,425 355,465" fill="url(#steel)"/>
    <polygon class="photo-swiss" role="img" aria-label="Photo of a Swiss-type machine cutting a steel bar"
      points="370,160 625,132 810,380 570,420" fill="url(#steel)"/>
    <polygon class="photo-five-axis" role="img" aria-label="Photo of a 5-axis machine milling with coolant spray"
      points="690,145 960,115 960,330 845,365" fill="url(#steel)"/>

    <!-- service labels -->
    <polygon class="label-band" points="105,175 310,150 335,185 130,210" fill="var(--label)" opacity="0.92"/>
    <text class="service-label" x="150" y="200">MILLING</text>

    <polygon class="label-band" points="690,145 960,115 960,150 712,180" fill="var(--label)" opacity="0.92"/>
    <text class="service-label" x="795" y="165">5-AXIS</text>

    <polygon class="label-band" points="565,385 800,343 822,382 585,424" fill="var(--label)" opacity="0.92"/>
    <text class="service-label" x="655" y="398">SWISS</text>

    <polygon class="label-band" points="0,470 285,430 322,470 0,520" fill="var(--label)" opacity="0.92"/>
    <text class="service-label" x="40" y="480">LATHE / TURNING</text>

    <!-- headline panel -->
    <polygon class="headline-panel" points="0,540 560,455 520,625 0,625" fill="url(#dark-panel)"/>
    <line x1="48" y1="552" x2="48" y2="604" stroke="var(--white)" stroke-width="2"/>
    <text class="headline-kicker" x="62" y="552">MACHINING</text>
    <text class="headline-main" x="62" y="580">COMPUTER NUMERIC</text>
    <text class="headline-main" x="62" y="608">CONTROL (CNC)</text>

    <!-- contact band -->
    <polygon class="contact-band" points="585,470 960,420 960,478 565,528" fill="var(--teal)"/>
    <g class="globe-icon" fill="none" stroke="var(--white)" stroke-width="1.5">
      <circle cx="640" cy="496" r="10"/>
      <ellipse cx="640" cy="496" rx="4.5" ry="10"/>
      <line x1="630" y1="496" x2="650" y2="496"/>
    </g>
    <text class="web-address" x="672" y="502">www.ridgelinecontrols.ca</text>
  </svg>
</main>
</body>
</html>
```